Greeting Cards for all Occasions

We are a large church and are sending cards all the time for different occasions. We'd like to have 5 different cards designed that fit with our brand guidelines and logo (Attached). We'd like to have designs for the following 5x7 cards. Each title should be featured on the front, and the inside should be blank, with the back should feature the contact info below. Appropriate photos from Unsplash are welcomed.

1. Happy Birthday
2. Get Well Soon
3. Praying for You
4. Happy Anniversary
5. Thank You

Contact info to include on the back:
Meadowlight Church
4817 Brambling Avenue, Corona, CA 92879
www.MeadowlightChurch.example I 909-555-0183

```html
<!DOCTYPE html>
<html lang="en">
<head>
<meta charset="utf-8">
<title>Meadowlight Church – Card Back</title>
<link href="https://fonts.googleapis.com/css2?family=Nunito+Sans:wght@400;700;800&display=swap" rel="stylesheet">
<style>
  :root {
    --backdrop: #aeaaa2;
    --card: #f3f3f3;
    --ink: #1c1c1c;
    --rule: #3a3a3a;
  }
  * { margin: 0; padding: 0; box-sizing: border-box; }
  html, body {
    width: 1200px;
    height: 800px;
    overflow: hidden;
    background: var(--backdrop);
    font-family: "Nunito Sans", sans-serif;
    color: var(--ink);
  }
  .canvas {
    position: relative;
    width: 1200px;
    height: 800px;
    display: flex;
    align-items: center;
    justify-content: center;
  }
  .card-back {
    position: relative;
    width: 440px;
    height: 616px;
    background: var(--card);
    display: flex;
    flex-direction: column;
    align-items: center;
  }
  .brand-mark {
    position: absolute;
    top: 218px;
    left: 0;
    right: 0;
    display: flex;
    align-items: center;
    justify-content: center;
    gap: 8px;
    font-weight: 800;
    font-size: 15px;
    letter-spacing: 0.02em;
  }
  .brand-mark .dot {
    width: 14px;
    height: 14px;
    border-radius: 50%;
    background: var(--ink);
  }
  .contact {
    position: absolute;
    bottom: 44px;
    left: 0;
    right: 0;
    text-align: center;
  }
  .contact-name {
    display: flex;
    align-items: center;
    justify-content: center;
    gap: 10px;
    font-weight: 800;
    font-size: 12.5px;
    margin-bottom: 6px;
  }
  .contact-name .rule {
    width: 66px;
    height: 1px;
    background: var(--rule);
  }
  .contact-line {
    font-size: 11px;
    line-height: 15px;
    font-weight: 400;
  }
</style>
</head>
<body>
  <main class="canvas">
    <section class="card-back">
      <div class="brand-mark"><span class="dot"></span>Meadowlight Church</div>
      <footer class="contact">
        <div class="contact-name"><span class="rule"></span>Meadowlight Church<span class="rule"></span></div>
        <p class="contact-line">4817 Brambling Avenue, Corona, CA 92879</p>
        <p class="contact-line">www.MeadowlightChurch.example I 909-555-0183</p>
      </footer>
    </section>
  </main>
</body>
</html>
```